Business Card and Stationary Design

After the successful redesign of our logo we are wanting to follow suite and create a new business card and stationary design!

New Logo is attached, information required on the business card should contain a mixture of the following but layout/arrangement is up to the designer.

Happy if the national provider number and abn are on the back, and happy for them to be smaller than the rest.

I am also happy to receive single sided or weird and wonderful designs.

Name
Title
National Provider Number 7291
ABN 53 219 864 317
Level 3, 42 Marlow Street
Brackley NSW 2316
Ph: 1300 987 214
Mobile: 0432 785 619
name@ferngatebuild.com.au
www.ferngatebuild.com.au

Target Market(s)

Professionals, Peers, Students, Suppliers...

Industry/Entity Type

Construction

Contact Information for Business Card

Listed in project description

Font styles to use
Other font styles liked:
• Century Gothic

Colors
0455a3
3176b5
ffffff

Requirements
Must have
• Professional Design, same color scheme as our logo
Nice to have
• Something that sets our apart from everyone else would be fantastic, open to size and shape and layout options, as long as they present professionally.
• Open to raised/embossed text, alternative materials, custom sizes, clear material
Should not have
• The color orange

```html
<!DOCTYPE html>
<html lang="en">
<head>
<meta charset="utf-8">
<title>ferngatebuild — Business Card</title>
<link href="https://fonts.googleapis.com/css2?family=Questrial&display=swap" rel="stylesheet">
<style>
  :root {
    --brand-dark: #0455a3;
    --brand-mid: #3176b5;
    --brand-navy: #1f3f9a;
    --brand-light: #4aa3dc;
    --paper: #ffffff;
    --ink: #2a2a2a;
    --muted: #555b63;
    --stage: #e9e9eb;
  }
  * { box-sizing: border-box; margin: 0; padding: 0; }
  html, body {
    width: 1200px; height: 1023px; overflow: hidden;
    background: var(--stage);
    font-family: "Questrial", "Century Gothic", sans-serif;
  }
  .sheet {
    width: 1200px; height: 1023px;
    display: flex; flex-direction: column; align-items: center; justify-content: center; gap: 60px;
  }
  .card {
    position: relative; width: 580px; height: 331px;
    border-radius: 26px; overflow: hidden;
    box-shadow: 0 6px 18px rgba(0,0,0,.18);
  }

  /* Front */
  .card-front { background: var(--paper); color: var(--ink); }
  .brand {
    position: absolute; left: 40px; top: 34px;
    display: flex; align-items: center; gap: 10px;
  }
  .brand-square { width: 22px; height: 22px; background: var(--brand-navy); }
  .brand-name { font-size: 30px; color: var(--brand-navy); letter-spacing: .3px; line-height: 1; }
  .registration {
    position: absolute; left: 72px; top: 70px;
    font-size: 11.5px; color: var(--muted); line-height: 1.45;
  }
  .person { position: absolute; left: 40px; top: 140px; }
  .person-name { font-size: 31px; color: var(--brand-navy); letter-spacing: .5px; line-height: 1; }
  .person-title { font-size: 14px; color: var(--ink); margin-top: 4px; letter-spacing: .4px; }
  .address {
    position: absolute; right: 40px; top: 140px; text-align: right;
    font-size: 14px; color: var(--ink); line-height: 1.55;
  }
  .rule {
    position: absolute; left: 40px; right: 40px; top: 196px;
    height: 1px; background: var(--brand-navy);
  }
  .contacts {
    position: absolute; left: 40px; top: 204px; list-style: none;
    font-size: 14px; color: var(--ink); line-height: 20px;
  }
  .contacts li { display: flex; align-items: center; gap: 8px; }
  .contacts svg { width: 12px; height: 12px; fill: var(--brand-navy); flex: none; }
  .band-thin { position: absolute; left: 0; right: 0; bottom: 26px; height: 5px; background: var(--brand-navy); }
  .band-thick { position: absolute; left: 0; right: 0; bottom: 0; height: 18px; background: var(--brand-navy); }

  /* Back */
  .card-back {
    background: radial-gradient(ellipse at 60% 45%, var(--brand-light) 0%, var(--brand-mid) 40%, var(--brand-dark) 100%);
    color: var(--paper);
  }
  .back-brand {
    position: absolute; left: 44px; bottom: 52px;
    display: flex; align-items: center; gap: 10px;
  }
  .back-brand .brand-square { background: var(--paper); }
  .back-brand .brand-name { color: var(--paper); font-size: 32px; }
  .back-web { position: absolute; left: 44px; bottom: 28px; font-size: 15px; letter-spacing: .5px; }
</style>
</head>
<body>
<main class="sheet">
  <section class="card card-front" aria-label="Business card front">
    <div class="brand">
      <span class="brand-square"></span>
      <span class="brand-name">ferngatebuild</span>
    </div>
    <div class="registration">
      <p>National Provider Number 7291</p>
      <p>ABN 53 219 864 317</p>
    </div>
    <div class="person">
      <p class="person-name">MARLA QUENBY</p>
      <p class="person-title">MANAGING DIRECTOR</p>
    </div>
    <div class="address">
      <p>Level 3, 42 Marlow Street</p>
      <p>Brackley NSW 2316</p>
    </div>
    <div class="rule"></div>
    <ul class="contacts">
      <li><svg viewBox="0 0 12 12"><path d="M2.5 1l2 2-1 1.5c.6 1.4 1.6 2.4 3 3L8 6.5l2 2-1.2 1.8C5 10 2 7 1.7 3.2z"/></svg>1300 987 214</li>
      <li><svg viewBox="0 0 12 12"><path d="M3 .5h6v11H3zM4 1.8v7.4h4V1.8z"/></svg>0432 785 619</li>
      <li><svg viewBox="0 0 12 12"><path d="M.5 2.5h11v7H.5zM1.5 3.3L6 6.5l4.5-3.2v-.1h-9z"/></svg>name@ferngatebuild.com.au</li>
      <li><svg viewBox="0 0 12 12"><path d="M6 .5a5.5 5.5 0 1 0 0 11A5.5 5.5 0 0 0 6 .5zm0 1c.8 0 1.6 1.6 1.8 4H4.2C4.4 3.1 5.2 1.5 6 1.5zM4.2 6.5h3.6c-.2 2.4-1 4-1.8 4s-1.6-1.6-1.8-4zM1.5 6.5h1.7c.1 1.4.4 2.6.9 3.4A4.5 4.5 0 0 1 1.5 6.5zm0-1a4.5 4.5 0 0 1 2.6-3.4c-.5.8-.8 2-.9 3.4zm7.3 0c-.1-1.4-.4-2.6-.9-3.4a4.5 4.5 0 0 1 2.6 3.4zm0 1h1.7a4.5 4.5 0 0 1-2.6 3.4c.5-.8.8-2 .9-3.4z"/></svg>www.ferngatebuild.com.au</li>
    </ul>
    <div class="band-thin"></div>
    <div class="band-thick"></div>
  </section>

  <section class="card card-back" aria-label="Business card back">
    <div class="back-brand">
      <span class="brand-square"></span>
      <span class="brand-name">ferngatebuild</span>
    </div>
    <p class="back-web">www.ferngatebuild.com.au</p>
  </section>
</main>
</body>
</html>
```